TELVORIQ HOA Portal Site for Public

Clean up and organize current website; need website to look good and functional; this is a HOA (homeowner association management) website where homeowners can login and pay their bill, general information about a HOA, monthly newsletter page.
Competitors:
https://plumbrivet.com/
https://duskorrahill.com/
https://www.qxlivingspan.com/nevada
http://www.bpt-hoa.com/

Target Market(s)

homeowners

Industry/Entity Type

Real Estate

Coding

Coded - Design and coding required

Number of Pages Required

5+ page

Font styles to use
Serif

Colors
0292cd
33a6d7
e667a6
e34297

Requirements
Must have
• login to pay
• services page
• contact us
• order resale package
Nice to have
• page why an HOA would contract us

```html
<!DOCTYPE html>
<html lang="en">
<head>
<meta charset="utf-8">
<title>Telvoriq Association Management</title>
<link rel="stylesheet" href="https://fonts.googleapis.com/css2?family=Montserrat:wght@400;500;600;700&family=Open+Sans:wght@400;600&family=Roboto:wght@400;700&display=swap">
<style>
:root{
  --blue:#0292cd;
  --blue-light:#33a6d7;
  --pink:#e34297;
  --pink-soft:#e667a6;
  --ink:#222;
  --text:#555;
  --grey-bg:#f4f4f4;
  --black:#000;
  --white:#fff;
  --head:'Montserrat',sans-serif;
  --body:'Open Sans',sans-serif;
}
*{box-sizing:border-box;margin:0;padding:0}
html,body{width:1200px;height:4713px;overflow:hidden}
body{position:relative;font-family:var(--body);color:var(--text);background:var(--white)}
.abs{position:absolute}
.center{left:0;width:1200px;text-align:center}
.btn{position:absolute;display:flex;align-items:center;justify-content:center;background:var(--pink);color:var(--white);font-family:var(--head);font-weight:600;text-transform:uppercase;font-size:20px;letter-spacing:.5px}
.section-title{position:absolute;left:0;width:1200px;text-align:center;font-family:var(--head);font-weight:700;color:var(--blue);font-size:35px;letter-spacing:.5px;text-transform:uppercase}
.section-sub{position:absolute;left:0;width:1200px;text-align:center;font-size:16px;color:var(--text)}

/* top bar + header */
.topbar{top:0;left:0;width:1200px;height:41px;background:var(--black)}
.topbar .phone{position:absolute;right:96px;top:8px;color:var(--white);font-family:var(--head);font-weight:600;font-size:22px;display:flex;align-items:center;gap:8px}
.header{top:41px;left:0;width:1200px;height:136px;background:var(--white);border-bottom:1px solid #e5e5e5}
.brand{position:absolute;left:88px;top:48px;display:flex;align-items:center;gap:10px}
.brand-mark{width:30px;height:30px;background:#6db33f}
.brand-name{font-family:var(--head);font-weight:700;font-size:15px;color:var(--ink);letter-spacing:.3px;text-transform:uppercase}
.nav{position:absolute;top:63px;left:0;width:1200px;font-family:var(--head);font-weight:500;font-size:18px;color:var(--ink)}
.nav span{position:absolute}
.nav .active{color:var(--blue-light);text-decoration:underline}

/* hero */
.hero{top:177px;left:0;width:1200px;height:582px;background:linear-gradient(180deg,#6f8fae 0%,#8b9a9c 25%,#5d6a5f 50%,#33482c 75%,#263820 100%)}
.hero h1{position:absolute;top:213px;left:0;width:1200px;text-align:center;color:var(--white);font-family:var(--head);font-weight:600;font-size:47px;letter-spacing:.5px}
.hero .btn{left:474px;top:293px;width:234px;height:60px;font-size:23px}

/* services */
.service-tile{position:absolute;top:947px;width:245px;height:236px}
.service-emergency{background:var(--blue-light);color:var(--white);display:flex;align-items:center;justify-content:center;text-align:center;font-family:var(--head);font-size:27px;line-height:1.2}

/* about */
.about{top:1353px;left:0;width:1200px;height:580px;background:var(--blue)}
.about-photo{position:absolute;left:0;top:0}
.about h2{position:absolute;left:558px;top:128px;color:var(--white);font-family:var(--head);font-weight:600;font-size:35px;letter-spacing:1px}
.about p{position:absolute;left:558px;top:200px;width:508px;color:var(--white);font-size:16.5px;line-height:32px;text-align:justify}
.about .btn{left:558px;top:449px;width:185px;height:49px;font-size:19px}

/* videos */
.video{position:absolute;top:2109px;width:324px;height:207px}
.video .play{position:absolute;left:50%;top:50%;width:40px;height:40px;margin:-20px 0 0 -20px;border-radius:50%;background:var(--white)}
.video-caption{position:absolute;top:2333px;width:324px;text-align:center;font-family:var(--head);font-weight:600;font-size:15.5px;line-height:27px;color:var(--ink);text-transform:uppercase}

/* help band */
.help{top:2543px;left:0;width:1200px;height:254px;background:var(--blue-light)}
.help h2{position:absolute;top:35px;left:0;width:1200px;text-align:center;color:var(--white);font-family:var(--head);font-weight:600;font-size:35px;line-height:50px;letter-spacing:1.5px}
.help .outline{position:absolute;left:476px;top:159px;width:243px;height:62px;border:2px solid var(--white);color:var(--white);display:flex;align-items:center;justify-content:center;font-family:var(--head);font-size:26px;letter-spacing:1px}

/* testimonials */
.testimonial{position:absolute;top:2945px;width:308px;height:265px;background:var(--white);border:2px solid #e3e3e3;border-radius:6px;box-shadow:0 4px 14px rgba(0,0,0,.08)}
.testimonial .avatar{position:absolute;left:20px;top:24px;width:52px;height:36px;border-radius:4px;background:#b99a83}
.testimonial .name{position:absolute;left:84px;top:24px;font-family:var(--head);font-weight:600;font-size:17.5px;color:var(--blue-light);text-transform:uppercase}
.testimonial .org{position:absolute;left:84px;top:49px;font-family:var(--head);font-weight:700;font-size:10px;color:#555}
.testimonial p{position:absolute;left:20px;top:102px;width:268px;font-size:13.5px;line-height:25px;color:#666;text-align:justify}
.testimonial .quote{position:absolute;right:16px;bottom:-16px}
.arrow{position:absolute;top:3230px}

/* events */
.events{top:3311px;left:0;width:1200px;height:594px;background:var(--grey-bg)}
.event{position:absolute;top:3477px;width:329px;height:383px;background:var(--blue-light)}
.event .photo{height:181px}
.event .meta{position:absolute;left:16px;top:195px;display:flex;gap:14px;color:var(--white);font-size:13px;align-items:center}
.event .meta span{display:flex;align-items:center;gap:6px}
.event h3{position:absolute;left:16px;top:230px;width:300px;color:var(--white);font-family:'Roboto',sans-serif;font-weight:700;font-size:22px;line-height:32px}
.event .more{position:absolute;left:16px;top:312px;width:116px;height:32px;border:2px solid var(--white);color:var(--white);font-family:'Roboto',sans-serif;font-weight:700;font-size:14px;display:flex;align-items:center;justify-content:center}

/* contact + footer */
.footer{top:4373px;left:0;width:1200px;height:340px;background:var(--black)}
.contact-card{top:3965px;left:123px;width:953px;height:575px;background:var(--white);box-shadow:0 0 18px rgba(0,0,0,.12)}
.contact-card h2{position:absolute;top:68px;left:0;width:953px;text-align:center;font-family:var(--head);font-weight:700;color:var(--blue-light);font-size:38px}
.info{position:absolute;left:58px;top:145px;width:289px;height:371px;background:var(--blue-light);color:var(--white)}
.info h3{position:absolute;top:68px;left:0;width:289px;text-align:center;font-family:var(--head);font-weight:600;font-size:20px}
.info .row{position:absolute;left:0;width:289px;display:flex;gap:22px;padding-left:28px;font-size:14px;line-height:26px;border-bottom:1px solid rgba(255,255,255,.35)}
.form{position:absolute;left:382px;top:182px;width:455px}
.form h4{font-family:var(--head);font-weight:600;color:var(--blue-light);font-size:19px;margin-bottom:24px}
.field{font-size:14px;color:#444;border-bottom:1px solid #777;height:26px;margin-bottom:24px}
.field.msg{height:48px}
.captcha{position:absolute;left:382px;top:466px;width:212px;height:52px;border:1px solid #ccc;background:#f9f9f9;display:flex;align-items:center;gap:12px;padding-left:12px;font-size:13px;color:#333}
.captcha i{width:24px;height:24px;border:2px solid #bbb;background:var(--white);display:block}
.submit{position:absolute;left:724px;top:474px;width:146px;height:40px;background:var(--pink);color:var(--white);font-family:var(--head);font-weight:600;font-size:17px;display:flex;align-items:center;justify-content:center;gap:18px}
.footer-nav{position:absolute;top:4598px;left:0;width:1200px;font-family:var(--head);font-size:18px;color:var(--white)}
.footer-nav span{position:absolute}
.copyright{position:absolute;top:4645px;left:0;width:1200px;text-align:center;color:var(--white);font-family:var(--head);font-size:16px}
</style>
</head>
<body>

<div class="abs topbar">
  <div class="phone">
    <svg width="14" height="14" viewBox="0 0 24 24"><path fill="#fff" d="M6.6 10.8a15 15 0 0 0 6.6 6.6l2.2-2.2c.3-.3.7-.4 1-.2 1.1.4 2.3.6 3.6.6.6 0 1 .4 1 1V20c0 .6-.4 1-1 1A17 17 0 0 1 3 4c0-.6.4-1 1-1h3.5c.6 0 1 .4 1 1 0 1.3.2 2.5.6 3.6.1.3 0 .7-.2 1z"/></svg>
    +1 702-555-0148
  </div>
</div>

<header class="abs header">
  <div class="brand"><span class="brand-mark"></span><span class="brand-name">Telvoriq Association Management</span></div>
  <nav class="nav">
    <span class="active" style="left:459px">Home</span>
    <span style="left:545px">About Us</span>
    <span style="left:658px">Events</span>
    <span style="left:749px">Services</span>
    <span style="left:856px">Southern Nevada</span>
    <span style="left:1039px">Contact</span>
  </nav>
</header>

<section class="abs hero" role="img" aria-label="Aerial photo of the city skyline with mountains behind">
  <h1>TELVORIQ ASSOCIATION MANAGEMENT</h1>
  <div class="btn">Login to Pay</div>
</section>

<section class="services">
  <h2 class="section-title" style="top:808px">Our Services</h2>
  <p class="section-sub" style="top:874px">Lorem ipsum dolor sit amet, consectetur adipiscing elit. Pellentesque vitae consequat urna. Fusce lacinia tortor in neque</p>
  <div class="service-tile" style="left:88px;background:linear-gradient(135deg,#d9d9d9,#6d6f74)" role="img" aria-label="Team joining hands in agreement"></div>
  <div class="service-tile" style="left:347px;background:linear-gradient(180deg,#a9c48e,#6b7c56 60%,#a08360)" role="img" aria-label="Smartphone showing a 24/7 service symbol"></div>
  <div class="service-tile service-emergency" style="left:605px">24 Hour<br>Emergency<br>service</div>
  <div class="service-tile" style="left:863px;background:linear-gradient(135deg,#f2f2f2,#e3d2b8 55%,#c9643f)" role="img" aria-label="Model house on a checklist"></div>
  <div class="btn" style="left:507px;top:1242px;width:184px;height:49px">View All</div>
</section>

<section class="abs about">
  <svg class="about-photo" width="520" height="580" role="img" aria-label="Group of community members outdoors at an event">
    <defs><linearGradient id="aboutPhoto" x1="0" y1="0" x2="1" y2="1"><stop offset="0" stop-color="#8aa35f"/><stop offset=".5" stop-color="#6b5a63"/><stop offset="1" stop-color="#4f6b3a"/></linearGradient></defs>
    <path d="M0 0H420C480 120 503 260 503 580H0Z" fill="url(#aboutPhoto)"/>
  </svg>
  <h2>ABOUT US</h2>
  <p>Telvoriq Association Management is a new company that is building on our experience with real estate sales and leasing, property management, and community association management. We understand the hard work involved in making an association run smoothly, and offer the tools and service to build a sense of community within your HOA.</p>
  <div class="btn">Read More</div>
</section>

<section class="videos">
  <h2 class="section-title" style="top:1982px">Telvoriq Association Management Videos</h2>
  <p class="section-sub" style="top:2050px">Every member of our team has a passion for being the best at what we do, and together, we create communities.</p>
  <div class="video" style="left:95px;background:linear-gradient(135deg,#3a3835,#1e1d1b)" role="img" aria-label="Video still of a presenter"><span class="play"></span></div>
  <div class="video" style="left:437px;background:linear-gradient(135deg,#6d655c,#2c2a28)" role="img" aria-label="Video still of two businessmen"><span class="play"></span></div>
  <div class="video" style="left:779px;background:linear-gradient(135deg,#2f6a8a,#1d4660)" role="img" aria-label="Video still of a partner brand intro"><span class="play"></span></div>
  <div class="video-caption" style="left:95px">Telvoriq Association<br>Management Exceeds Customer<br>Expectations Every Day</div>
  <div class="video-caption" style="left:437px">Telvoriq Association<br>Management</div>
  <div class="video-caption" style="left:779px">Brand Creative Video</div>
  <div class="btn" style="left:516px;top:2431px;width:186px;height:49px">View More</div>
</section>

<section class="abs help">
  <h2>WE ARE HERE TO HELP<br>24/7 OUR SUPPORT STAFF IS READY</h2>
  <div class="outline">CONTACT US</div>
</section>

<section class="testimonials">
  <h2 class="section-title" style="top:2845px">Testimonials</h2>
  <div class="testimonial" style="left:104px">
    <span class="avatar"></span><span class="name">Nolan Brisket</span><span class="org">TELVORIQ HOA.</span>
    <p>Lorem ipsum dolor sit amet, consectetur adipiscing elit. Phasellus efficitur iaculis vulputate. Vestibulum ante ipsum primis.</p>
    <svg class="quote" width="56" height="40" viewBox="0 0 56 40"><path fill="#fff" stroke="#ccc" stroke-width="3" d="M4 4h20v18c0 8-6 14-14 14v-6c4 0 6-3 6-8H4zM32 4h20v18c0 8-6 14-14 14v-6c4 0 6-3 6-8H32z"/></svg>
  </div>
  <div class="testimonial" style="left:437px;border-color:#f0f0f0">
    <span class="avatar" style="background:#c7a58b"></span><span class="name">Wanda Ferrow</span><span class="org">TELVORIQ HOA.</span>
    <p>Lorem ipsum dolor sit amet, consectetur adipiscing elit. Phasellus efficitur iaculis vulputate. Vestibulum ante ipsum primis.</p>
    <svg class="quote" width="56" height="40" viewBox="0 0 56 40"><path fill="#fff" stroke="#ccc" stroke-width="3" d="M4 4h20v18c0 8-6 14-14 14v-6c4 0 6-3 6-8H4zM32 4h20v18c0 8-6 14-14 14v-6c4 0 6-3 6-8H32z"/></svg>
  </div>
  <div class="testimonial" style="left:765px">
    <span class="avatar" style="background:#a58b77"></span><span class="name">Otis Quillby</span><span class="org">TELVORIQ HOA.</span>
    <p>Lorem ipsum dolor sit amet, consectetur adipiscing elit. Phasellus efficitur iaculis vulputate. Vestibulum ante ipsum primis.</p>
    <svg class="quote" width="56" height="40" viewBox="0 0 56 40"><path fill="#fff" stroke="#ccc" stroke-width="3" d="M4 4h20v18c0 8-6 14-14 14v-6c4 0 6-3 6-8H4zM32 4h20v18c0 8-6 14-14 14v-6c4 0 6-3 6-8H32z"/></svg>
  </div>
  <svg class="arrow" style="left:94px" width="18" height="18" viewBox="0 0 18 18"><path d="M16 9H3M8 3L2 9l6 6" stroke="#111" stroke-width="2.4" fill="none"/></svg>
  <svg class="arrow" style="left:1091px" width="18" height="18" viewBox="0 0 18 18"><path d="M2 9h13M10 3l6 6-6 6" stroke="#111" stroke-width="2.4" fill="none"/></svg>
</section>

<section class="abs events"></section>
<h2 class="section-title" style="top:3350px">Events</h2>
<p class="section-sub" style="top:3410px">Every member of our team has a passion for being the best at what we do, and together.</p>

<article class="event" style="left:88px">
  <div class="photo" style="background:linear-gradient(180deg,#7ca7d6,#5d8a3a)" role="img" aria-label="Bounce house and inflatable slide at a community party"></div>
  <div class="meta"><span><svg width="13" height="13" viewBox="0 0 14 14"><circle cx="7" cy="7" r="6" stroke="#fff" fill="none" stroke-width="1.5"/><circle cx="7" cy="5.5" r="2" fill="#fff"/></svg>Marla Ostrand</span><span><svg width="13" height="13" viewBox="0 0 14 14"><rect x="1" y="2" width="12" height="11" fill="none" stroke="#fff" stroke-width="1.5"/><path d="M1 5h12" stroke="#fff" stroke-width="1.5"/></svg>August 9, 2019</span></div>
  <h3>Neque porro quisquamest qui dolorem</h3>
  <div class="more">Read More</div>
</article>
<article class="event" style="left:432px">
  <div class="photo" style="background:linear-gradient(180deg,#6b6e78,#2a2a2e)" role="img" aria-label="Grills cooking at an outdoor barbecue"></div>
  <div class="meta"><span><svg width="13" height="13" viewBox="0 0 14 14"><circle cx="7" cy="7" r="6" stroke="#fff" fill="none" stroke-width="1.5"/><circle cx="7" cy="5.5" r="2" fill="#fff"/></svg>Cal Renwick</span><span><svg width="13" height="13" viewBox="0 0 14 14"><rect x="1" y="2" width="12" height="11" fill="none" stroke="#fff" stroke-width="1.5"/><path d="M1 5h12" stroke="#fff" stroke-width="1.5"/></svg>August 9, 2019</span></div>
  <h3>Neque porro quisquamest qui dolorem</h3>
  <div class="more">Read More</div>
</article>
<article class="event" style="left:777px">
  <div class="photo" style="background:linear-gradient(180deg,#6f9c5a,#2c57a8)" role="img" aria-label="Volunteers in blue shirts at a neighborhood event"></div>
  <div class="meta"><span><svg width="13" height="13" viewBox="0 0 14 14"><circle cx="7" cy="7" r="6" stroke="#fff" fill="none" stroke-width="1.5"/><circle cx="7" cy="5.5" r="2" fill="#fff"/></svg>Cal Renwick</span><span><svg width="13" height="13" viewBox="0 0 14 14"><rect x="1" y="2" width="12" height="11" fill="none" stroke="#fff" stroke-width="1.5"/><path d="M1 5h12" stroke="#fff" stroke-width="1.5"/></svg>August 9, 2019</span></div>
  <h3>Neque porro quisquamest qui dolorem</h3>
  <div class="more">Read More</div>
</article>

<footer class="abs footer"></footer>

<section class="abs contact-card">
  <h2>CONTACT US</h2>
  <div class="info">
    <h3>GET IN TOUCH</h3>
    <div class="row" style="top:120px;height:82px;padding-top:12px"><svg width="14" height="18" viewBox="0 0 14 18"><path fill="#fff" d="M7 0a7 7 0 0 1 7 7c0 5-7 11-7 11S0 12 0 7a7 7 0 0 1 7-7zm0 4a3 3 0 1 0 0 6 3 3 0 0 0 0-6z"/></svg><span>4870 Larkspan Rd., Ste 310<br>Henderson, Nevada</span></div>
    <div class="row" style="top:202px;height:54px;align-items:center"><svg width="16" height="16" viewBox="0 0 24 24"><path fill="#fff" d="M6.6 10.8a15 15 0 0 0 6.6 6.6l2.2-2.2c.3-.3.7-.4 1-.2 1.1.4 2.3.6 3.6.6.6 0 1 .4 1 1V20c0 .6-.4 1-1 1A17 17 0 0 1 3 4c0-.6.4-1 1-1h3.5c.6 0 1 .4 1 1 0 1.3.2 2.5.6 3.6.1.3 0 .7-.2 1z"/></svg><span>+1 702-555-0148</span></div>
    <div class="row" style="top:256px;height:56px;align-items:center"><svg width="16" height="14" viewBox="0 0 16 14"><rect x="1" y="1" width="14" height="12" fill="none" stroke="#fff" stroke-width="1.6"/><path d="M1 2l7 6 7-6" fill="none" stroke="#fff" stroke-width="1.6"/></svg><span>hello@telvoriq.com</span></div>
  </div>
  <div class="form">
    <h4>LET'S TALK</h4>
    <div class="field">Your Name</div>
    <div class="field">Email Address</div>
    <div class="field">Phone Number</div>
    <div class="field msg">Message</div>
  </div>
  <div class="captcha"><i></i>I'm not a Robot</div>
  <div class="submit">Submit <span>›</span></div>
</section>

<nav class="footer-nav">
  <span style="left:215px">Home</span>
  <span style="left:343px">About Us</span>
  <span style="left:497px">Events</span>
  <span style="left:630px">Services</span>
  <span style="left:778px">Southern Nevada</span>
  <span style="left:1002px">Contact</span>
</nav>
<p class="copyright">Copyright © 2019 Telvoriq Association Management.All Rights Reserved</p>

</body>
</html>
```